Amber Thistle Gin needs a bottle label

We need help designing a Gin Bottle label for our new Super Premium Gin; "Amber Thistle." Our new Distillery, Dunmore & Keane, Artisan Irish Distillers is based in the Historic Glenfallow House in County Carlow, Ireland.
This gin will be produced in small artisan batches and each bottle individually signed, dated and batch numbered. This must be allowed for somewhere on the label, either front or back.

Our Label needs to be both Elegant, Serious, Upmarket and Personable.
It may also be a see through label letting people see through to the back label.

It needs to incorporate Our Amber Thistle. (See attached images and supporting Documentation.) Also, the front and back labels will be going on a "Tavora Flask" Bottle, from Merlin Vitre in a 70cl Size. (Link to Tech Spec with Dimensions. http://www.merlinvitre-example.com/en/tavora-flask-70-cl-gpi-white)

Colours will include, Silver and Black. We are open to the addition of other colours but we want to make sure the label still looks premium. We are also open to embossing and also to wrap around inside back printed labels also.

The back will also incorporate a bar code and possibly a QR code. These can be placed within key shapes for stylization ie: a bottle or Glass. It will also have a few lines of who we are and a summary product description

Our Price Point is circa €50 per 70CL bottle. Thus a Super Premium expensive Gin.

Target Market(s)

We have detailed our "ideal" customer profile.
25-42 years old.
60% Female / 40% male.
High Disposable Income Bracket
Lives in Cities or the Suburbs.
Into higher cost Sports like, Horse Polo, Skiing, Surfing, Hunting etc

Requirements
Must have
• The colours silver and black.
• A premium look and feel.
• The Amber Thistle incorporated into the design.
• Space for signing, dating and batch number.
• Size of the bottle and alcohol percentage.
Nice to have
• Classy modern design.
• stylised bar code.
• Space for descriptive text on the back.

```html
<!DOCTYPE html>
<html lang="en">
<head>
<meta charset="utf-8">
<title>Amber Thistle Gin – Front Label</title>
<link rel="stylesheet" href="https://fonts.googleapis.com/css2?family=Cinzel:wght@400;600&family=Cormorant+Garamond:ital,wght@0,400;0,500;1,400&display=swap">
<style>
  :root {
    --page-bg: #f4f4f4;
    --label-black: #0b0b0b;
    --label-pattern-a: #171717;
    --label-pattern-b: #0e0e0e;
    --silver: #dcdcdc;
    --silver-soft: #a3a3a3;
    --silver-dim: #727272;
    --thistle-light: #c4c4c4;
    --thistle-dark: #3e3e3e;
  }
  * { margin: 0; padding: 0; box-sizing: border-box; }
  html, body {
    width: 1200px;
    height: 2824px;
    overflow: hidden;
    background: var(--page-bg);
  }
  .canvas {
    position: relative;
    width: 1200px;
    height: 2824px;
  }
  .front-label {
    position: absolute;
    left: 170px;
    top: 282px;
    width: 860px;
    height: 2260px;
    background: var(--label-black);
    overflow: hidden;
    color: var(--silver);
    text-align: center;
  }
  .label-pattern {
    position: absolute;
    inset: 0;
    background: radial-gradient(ellipse at 50% 30%, var(--label-pattern-a) 0%, var(--label-pattern-b) 55%, var(--label-black) 100%);
  }
  .thistle-emblem {
    position: absolute;
    left: 392px;
    top: 40px;
    width: 76px;
    height: 290px;
    border-radius: 34px 34px 10px 10px;
    background: linear-gradient(180deg, var(--thistle-light) 0%, var(--thistle-dark) 100%);
    opacity: 0.7;
  }
  .title-rule {
    position: absolute;
    left: 0;
    width: 860px;
    height: 20px;
  }
  .title-rule--top { top: 348px; }
  .title-rule--bottom { top: 456px; }
  .brand-name {
    position: absolute;
    left: 0;
    right: 0;
    top: 378px;
    font-family: "Cinzel", serif;
    font-weight: 600;
    font-size: 56px;
    letter-spacing: 2px;
    line-height: 66px;
    color: var(--silver);
  }
  .product-type {
    position: absolute;
    left: 0;
    right: 0;
    top: 492px;
    font-family: "Cormorant Garamond", serif;
    font-size: 24px;
    line-height: 28px;
    color: var(--silver-soft);
  }
  .volume {
    position: absolute;
    left: 0;
    right: 0;
    top: 560px;
    font-family: "Cinzel", serif;
    font-size: 32px;
    line-height: 40px;
    color: var(--silver);
  }
  .volume .abv {
    font-size: 22px;
    color: var(--silver-soft);
    margin-left: 14px;
  }
  .batch-note {
    position: absolute;
    left: 250px;
    width: 360px;
    top: 1150px;
    font-family: "Cormorant Garamond", serif;
    font-size: 22px;
    line-height: 34px;
    color: var(--silver-soft);
  }
  .fill-line {
    display: inline-block;
    width: 70px;
    border-bottom: 1px solid var(--silver-dim);
    height: 22px;
    vertical-align: baseline;
  }
  .signing-field {
    position: absolute;
    left: 250px;
    width: 360px;
    top: 1330px;
    display: flex;
    justify-content: space-between;
    gap: 30px;
  }
  .signing-field__slot {
    flex: 1;
    border-top: 2px solid var(--silver-dim);
    padding-top: 8px;
    font-family: "Cormorant Garamond", serif;
    font-style: italic;
    font-size: 18px;
    color: var(--silver-dim);
  }
  .signing-field__slot--signature { flex: 1.6; }
  .story {
    position: absolute;
    left: 230px;
    width: 400px;
    top: 1500px;
    font-family: "Cormorant Garamond", serif;
    font-size: 21px;
    line-height: 39px;
    color: var(--silver-dim);
  }
</style>
</head>
<body>
<main class="canvas">
  <section class="front-label">
    <div class="label-pattern" role="img" aria-label="Faint dark swirling botanical pattern across the label background"></div>

    <div class="thistle-emblem" role="img" aria-label="Silver Amber Thistle illustration at the top of the label"></div>

    <svg class="title-rule title-rule--top" viewBox="0 0 860 20" aria-hidden="true">
      <line x1="215" y1="10" x2="645" y2="10" stroke="#a3a3a3" stroke-width="2"/>
      <circle cx="430" cy="10" r="4" fill="#dcdcdc"/>
    </svg>
    <h1 class="brand-name">Amber Thistle</h1>
    <svg class="title-rule title-rule--bottom" viewBox="0 0 860 20" aria-hidden="true">
      <line x1="215" y1="10" x2="645" y2="10" stroke="#a3a3a3" stroke-width="2"/>
      <circle cx="430" cy="10" r="4" fill="#dcdcdc"/>
    </svg>

    <p class="product-type">Premium<br>Gin</p>
    <p class="volume">0,70 L<span class="abv">42% vol</span></p>

    <p class="batch-note">This is bottle No. <span class="fill-line"></span> of Batch No. <span class="fill-line"></span> of our small batch Super Premium Gin</p>

    <div class="signing-field">
      <span class="signing-field__slot signing-field__slot--signature">Signed</span>
      <span class="signing-field__slot">Dated</span>
    </div>

    <p class="story">Distilled in small artisan batches at Glenfallow House, County Carlow, this gin unites fresh juniper, wild botanicals and a gentle warmth of citrus peel. Every run is tended by hand, slowly rested and bottled with care for those who savour a finer measure.</p>
  </section>
</main>
</body>
</html>
```